CraneHollow - Business Card and Letterhead

After having received some fantastic submissions in our recent logo design project, I would now like to extend our branding to letterheads and business cards.
CraneHollow is a consulting service in the Construction Industry. We deal with both residential and commercial projects, and our clients include Architects, Builders, Tradespeople and Home Owners.
The designs should be simple and effective, convey personal service and professionalism, and display some level of creativity.
For both the business cards and letterhead, a white card stock will be used. This project is for business cards and letterheads only. Our new logo is attached for use.
The designs should incorporate our two main colours which are Blue (RGB 14,92,143) and Green (RGB 132,194,37).
For the time being, please submit all designs showing generic information including name, mobile number, email, postal address and website details. No fax number or physical address is required. I will provide our actual contact details once a final design has been selected.
I encourage you to interpret this brief in your own creative way, and look forward to some quality submissions.
Thanks!
Leo
CraneHollow.

```html
<!DOCTYPE html>
<html lang="en">
<head>
<meta charset="utf-8">
<title>CraneHollow Letterhead</title>
<link href="https://fonts.googleapis.com/css2?family=Questrial&family=Lato:wght@700&display=swap" rel="stylesheet">
<style>
  :root {
    --brand-blue: #0e5c8f;
    --brand-green: #84c225;
    --ink: #2b2b2b;
    --paper: #ffffff;
    --backdrop: #e6e7e8;
    --signature-tone: #d6e0ef;
  }
  * { margin: 0; padding: 0; box-sizing: border-box; }
  html, body {
    width: 1200px; height: 900px; overflow: hidden;
    background: var(--backdrop);
  }
  .letterhead {
    position: absolute; left: 300px; top: 26px;
    width: 600px; height: 848px;
    background: var(--paper);
    box-shadow: 0 2px 10px rgba(0,0,0,0.15);
    font-family: "Questrial", sans-serif;
    color: var(--ink);
    overflow: hidden;
  }
  .brand {
    position: absolute; left: 43px; top: 46px;
    display: flex; align-items: center; gap: 7px;
  }
  .brand-square {
    width: 20px; height: 20px; background: var(--brand-green);
  }
  .brand-name {
    font-family: "Lato", sans-serif; font-weight: 700;
    font-size: 24px; color: var(--brand-blue); letter-spacing: -0.2px;
  }
  .contact {
    position: absolute; left: 324px; top: 43px;
    font-size: 8px; line-height: 9.3px;
    display: grid; grid-template-columns: auto auto; column-gap: 4px;
  }
  .contact dt { color: var(--brand-blue); }
  .contact dd { color: var(--ink); }
  .contact-divider {
    position: absolute; left: 450px; top: 42px;
    width: 1px; height: 33px; background: var(--brand-blue);
  }
  .address {
    position: absolute; left: 459px; top: 43px;
    font-size: 8px; line-height: 9.3px; font-style: normal;
  }
  .address .web { color: var(--brand-blue); }
  .letter-body {
    position: absolute; left: 86px; top: 282px; width: 428px;
    font-size: 11px; line-height: 13.3px; letter-spacing: 0.35px;
    text-align: justify;
  }
  .letter-body p + p { margin-top: 13.3px; }
  .signature {
    position: absolute; left: 80px; top: 630px;
    width: 150px; height: 30px;
    background: var(--signature-tone); border-radius: 4px;
  }
  .signatory-title {
    position: absolute; left: 86px; top: 666px;
    font-size: 11px; letter-spacing: 0.3px;
  }
  .footer-stripe {
    position: absolute; left: 0; bottom: 52px;
    width: 600px; height: 5px; background: var(--brand-green);
  }
  .footer-band {
    position: absolute; left: 0; bottom: 0;
    width: 600px; height: 46px; background: var(--brand-blue);
  }
</style>
</head>
<body>
  <main class="letterhead">
    <div class="brand">
      <span class="brand-square"></span>
      <span class="brand-name">CraneHollow</span>
    </div>

    <dl class="contact">
      <dt>phone</dt><dd>800 410 22 37</dd>
      <dt>mobile</dt><dd>541 302 77 19</dd>
      <dt>email</dt><dd>info@cranehollow.com</dd>
    </dl>
    <div class="contact-divider"></div>
    <address class="address">
      48 Millbrook Lane<br>
      Fairview, Oregon 97024<br>
      <span class="web">www.cranehollow.com</span>
    </address>

    <section class="letter-body">
      <p>Letterhead samples are a great way of deciding what kind of letterhead you want to design for you and your company. The internet has a ton of great letterhead samples to browse through. Whether you want something simple, with just a couple lines of text of your business information, or something decorative and stunning, with photos and logos on the top and bottom of the page, it will be easy to find what you want, because there are samples online for basically any type of letterhead you could want.</p>
      <p>Any business could easily benefit from browsing through some letterhead samples, if only to get an idea for what kind of letterhead their company might want. Letterheads are just one of the tools that a business professional could use to help increase their customer base, and to really be memorable to everyone they write a letter to. Letterhead is quite an effective tool for marketing and advertising, but because it’s such a simple and well known idea, it is often unfairly overlooked. Make sure you don’t make that mistake, and make some letterhead samples of your own today.</p>
      <p>Whether you want to get new customers to remember you and become part of your clientele, or you just want to send out friendly reminders to your existing clients, customizing your own letterhead samples can really help you out. Try out some letterhead samples and you will not regret it, and I’m sure you will add a new tool to your business’ arsenal of networking, marketing, and advertising tools.</p>
    </section>

    <div class="signature" role="img" aria-label="Handwritten signature of Martin Calloway"></div>
    <div class="signatory-title">company director</div>

    <div class="footer-stripe"></div>
    <div class="footer-band"></div>
  </main>
</body>
</html>
```